Business Card for Marriage Commissioner

I am a marriage commissioner in the province of Alberta, meaning that I perform civil unions here. I have been trying to think of a unique design for my business card, something a bit different. A lot of "unique" designs seem to incorporate unique cuts or "some assembly required" or printed on plastic or meat. I would like my design to be a full colour card that is a typical business card size.

The information on the card should have:
Lou Varnik
my occupation: Marriage Commissioner
my website: www.louvarnik.ca
my e-mail: lou@louvarnik.ca
my phone: 780-418-2964

I originally submitted a design to the printer that had a screen capture of a findly search window, with my name and occupation in the text box. And underneath that, my phone number. Nothing else. They indicated they could not print this because it was a copyright violation.

One option on the design is I am a retired chemist-so a chemistry themed card would also be of interest, as long as it isn't a "Rusted Tide" theme, as I have that on my other business cards already...

I would prefer a single sided card, but I am open to a double sided card if it is clever!

I would also prefer not to have pictures of male and female couples as in my position I will also marry same sex couples. Same thing for male/female symbols. Someone has submitted two graduated cylinders in love, which is very clever, and gets around this male/female type.

Thanks for your help and interest.

Target Market(s)

Young couples.

Industry/Entity Type

Plastic

Requirements
Nice to have
• chemistry ideas!
Should not have
• Male/female pictures, male/female symbols.
No QR codes.
No transparent designs, will go on paper stock.

```html
<!DOCTYPE html>
<html lang="en">
<head>
<meta charset="utf-8">
<title>Lou Varnik – Marriage Commissioner business card</title>
<link href="https://fonts.googleapis.com/css2?family=Arimo:wght@400;700&family=Oswald:wght@400;500&display=swap" rel="stylesheet">
<style>
  :root {
    --page-bg: #f2f2f2;
    --card-light: #ffffff;
    --card-mid: #dde2e5;
    --card-dark: #a3adb4;
    --ink: #0c0c0c;
    --ink-soft: #2c3034;
    --paper-white: #ffffff;
    --subtitle: #d6d6d6;
  }
  * { margin: 0; padding: 0; box-sizing: border-box; }
  html, body {
    width: 1200px; height: 801px; overflow: hidden;
    background: var(--page-bg);
  }
  .card {
    position: absolute; left: 100px; top: 115px;
    width: 1000px; height: 571px; overflow: hidden;
    background:
      radial-gradient(ellipse 70% 80% at 45% 35%, var(--card-light) 0%, var(--card-mid) 55%, var(--card-dark) 100%);
    box-shadow: 0 6px 18px rgba(0,0,0,0.12);
  }
  .accent-line {
    position: absolute; top: 0; width: 11px; height: 300px;
    background: var(--ink);
  }
  .accent-line--first { left: 820px; }
  .accent-line--second { left: 862px; }
  .name-bar {
    position: absolute; left: 0; top: 108px;
    width: 620px; height: 124px;
    background: var(--ink);
    border-radius: 0 26px 26px 0;
    padding: 10px 0 0 52px;
  }
  .name-bar__name {
    font-family: "Arimo", sans-serif; font-weight: 700;
    font-size: 64px; line-height: 64px; letter-spacing: 3px;
    text-transform: uppercase; color: var(--paper-white);
    font-variant: small-caps;
    text-shadow: 2px 2px 0 #555;
  }
  .name-bar__role {
    font-family: "Arimo", sans-serif; font-weight: 400;
    font-size: 40px; line-height: 44px; color: var(--subtitle);
    padding-left: 40px;
  }
  .contact-tab {
    position: absolute; left: 320px; top: 338px;
    width: 150px; height: 233px;
    background: var(--ink);
    border-radius: 24px 24px 0 0;
  }
  .contact-tab svg { position: absolute; left: 0; top: 0; }
  .contact-list {
    position: absolute; left: 496px; top: 342px;
    list-style: none;
    font-family: "Oswald", sans-serif; color: var(--ink-soft);
    text-shadow: 1px 1px 0 rgba(255,255,255,0.6), -1px -1px 0 rgba(0,0,0,0.25);
  }
  .contact-list__phone { font-size: 42px; line-height: 54px; font-weight: 500; }
  .contact-list__email { font-size: 32px; line-height: 58px; }
  .contact-list__web { font-size: 32px; line-height: 58px; }
</style>
</head>
<body>
  <div class="card">
    <div class="accent-line accent-line--first"></div>
    <div class="accent-line accent-line--second"></div>

    <div class="name-bar">
      <div class="name-bar__name">Lou Varnik</div>
      <div class="name-bar__role">Marriage Commissioner</div>
    </div>

    <div class="contact-tab" aria-hidden="true">
      <svg width="150" height="233" viewBox="0 0 150 233">
        <!-- phone -->
        <g fill="#fff" transform="translate(46,28)">
          <path d="M4 14 C4 4 52 4 52 14 L52 20 L40 20 L40 14 L16 14 L16 20 L4 20 Z"/>
          <path d="M14 20 L42 20 L50 40 L6 40 Z"/>
          <circle cx="28" cy="30" r="6" fill="#0c0c0c"/>
        </g>
        <!-- envelope -->
        <g transform="translate(52,104)">
          <rect x="0" y="0" width="46" height="30" fill="#fff"/>
          <path d="M0 0 L23 17 L46 0" fill="none" stroke="#0c0c0c" stroke-width="2.5"/>
        </g>
        <!-- globe -->
        <g transform="translate(77,183)" fill="none" stroke="#fff" stroke-width="3">
          <circle r="18"/>
          <ellipse rx="8" ry="18"/>
          <line x1="-18" y1="0" x2="18" y2="0"/>
          <line x1="-15" y1="-9" x2="15" y2="-9"/>
          <line x1="-15" y1="9" x2="15" y2="9"/>
        </g>
      </svg>
    </div>

    <ul class="contact-list">
      <li class="contact-list__phone">780-418-2964</li>
      <li class="contact-list__email">lou@louvarnik.ca</li>
      <li class="contact-list__web">www.louvarnik.ca</li>
    </ul>
  </div>
</body>
</html>
```